TKA Electricial Contracting Services

Hi guys, after a design for my small electrical company, have logo design files to be incorporated into the layout, the basic concept is electrical contracting services for residential, commercial, industrial & data services, image is clean clear and strong,

Card format is to have a nice clean logo on front,with maybe the Residential – commercial – industrial - data, followed with licensed & insured, followed by contact details on backside of the card.

Target Market(s)

Residential, commercial, industrial sectors.

Industry/Entity Type

Electrical

Contact Information for Business Card

TKA logo,
Residential – commercial – industrial - data
REC: 61372
Email: tka@poralink.net.au
Phone: 0458 203 719

Requirements
Must have
• Clean & strong design.
Nice to have
• If possible, I would like the logo colours inverted so the text is orange and the background is black on the front of the card, then the backside of the card be the reverse colour
Should not have
• No Sparks, lightning bolts,

```html
<!DOCTYPE html>
<html lang="en">
<head>
<meta charset="utf-8">
<title>TKA Electrical Services – Business Card</title>
<link rel="stylesheet" href="https://fonts.googleapis.com/css2?family=Exo+2:ital,wght@0,500;0,600;0,700;1,600;1,700&display=swap">
<style>
  :root {
    --orange: #f28a30;
    --orange-light: #f7a25a;
    --orange-deep: #ee7f22;
    --black: #0b0b0b;
    --charcoal: #1c1a19;
    --white: #ffffff;
    --band-line: #9a9a9a;
  }
  * { box-sizing: border-box; margin: 0; padding: 0; }
  html, body {
    width: 1200px; height: 1000px; overflow: hidden;
    background: var(--white);
    font-family: "Exo 2", sans-serif;
  }
  .canvas { position: relative; width: 1200px; height: 1000px; }

  /* Front of card */
  .card-front {
    position: absolute; left: 26px; top: 0; width: 812px; height: 474px;
    border-radius: 40px; overflow: hidden; background: var(--black);
  }
  .card-front .swoosh { position: absolute; inset: 0; }
  .card-front .circuit-area {
    position: absolute; left: 560px; top: 130px; width: 252px; height: 320px;
    background: radial-gradient(ellipse at 60% 50%, rgba(60,56,54,0.55), rgba(28,26,25,0) 70%);
  }
  .front-wordmark {
    position: absolute; left: 150px; top: 52px;
    font-size: 200px; font-weight: 600; line-height: 1; letter-spacing: -4px;
    color: var(--orange);
  }
  .front-company {
    position: absolute; left: 182px; top: 252px;
    font-size: 33px; font-weight: 600; color: var(--orange); letter-spacing: 0.5px;
  }
  .front-sectors, .front-licence {
    position: absolute; left: 0; width: 812px; text-align: center;
    font-size: 20px; font-weight: 600; color: var(--orange); letter-spacing: 0.8px;
  }
  .front-sectors { top: 335px; padding-left: 30px; }
  .front-licence { top: 366px; padding-left: 30px; }

  /* Back of card */
  .card-back {
    position: absolute; left: 302px; top: 491px; width: 870px; height: 509px;
    border-radius: 40px; overflow: hidden;
    background: linear-gradient(180deg, var(--orange-deep) 0%, var(--orange) 35%, var(--orange-light) 60%, var(--orange) 100%);
  }
  .back-glow {
    position: absolute; left: 200px; top: 0; width: 700px; height: 410px;
    background: radial-gradient(ellipse at 60% 55%, rgba(255,255,255,0.14), rgba(255,255,255,0) 65%);
  }
  .person-name {
    position: absolute; left: 41px; top: 90px;
    font-size: 32px; font-weight: 700; color: var(--black); letter-spacing: 0.5px; word-spacing: 6px;
  }
  .person-position {
    position: absolute; left: 43px; top: 131px;
    font-size: 27px; font-weight: 700; font-style: italic; color: var(--black); letter-spacing: 2px;
  }
  .contact-list { position: absolute; left: 41px; top: 186px; list-style: none; }
  .contact-list li {
    font-size: 28px; font-weight: 600; color: var(--white);
    line-height: 37px; letter-spacing: 0.6px;
  }
  .back-wordmark {
    position: absolute; right: 48px; top: 18px;
    font-size: 132px; font-weight: 600; line-height: 1; letter-spacing: -3px; color: var(--black);
  }
  .back-company {
    position: absolute; right: 52px; top: 144px;
    font-size: 22px; font-weight: 600; color: var(--black); letter-spacing: 0.4px;
  }
  .back-sectors, .back-rec {
    position: absolute; left: 0; width: 870px; text-align: center; color: var(--white);
  }
  .back-sectors { top: 351px; padding-left: 30px; font-size: 21px; font-weight: 600; letter-spacing: 1.6px; }
  .back-rec { top: 378px; padding-left: 30px; font-size: 21px; font-weight: 600; font-style: italic; letter-spacing: 0.8px; }
  .service-band {
    position: absolute; left: 0; bottom: 0; width: 870px; height: 97px;
    background: var(--black); border-top: 4px solid var(--band-line);
    text-align: center; padding-top: 27px; color: var(--white);
    font-style: italic; font-weight: 600; font-size: 24px; line-height: 31px;
  }
</style>
</head>
<body>
<main class="canvas">

  <section class="card-front" aria-label="Card front">
    <svg class="swoosh" width="812" height="474" viewBox="0 0 812 474" aria-hidden="true">
      <path d="M812 0 L560 0 C430 60 390 200 400 300 C410 400 470 460 520 474 L812 474 Z" fill="#1c1a19"/>
    </svg>
    <div class="circuit-area" role="img" aria-label="Faint circuit board trace decoration"></div>
    <div class="front-wordmark">TKA</div>
    <div class="front-company">TKA Electrical Services</div>
    <p class="front-sectors">Residential • Commercial • Industrial</p>
    <p class="front-licence">Licensed &amp; Insured</p>
  </section>

  <section class="card-back" aria-label="Card back">
    <div class="back-glow"></div>
    <div class="back-wordmark">TKA</div>
    <div class="back-company">TKA Electrical Services</div>
    <h1 class="person-name">First Name Surname</h1>
    <p class="person-position">POSITION</p>
    <ul class="contact-list">
      <li>Tel : XXXX XXX XXX</li>
      <li>Fax : XXXX XXX XXX</li>
      <li>Mob : 0458 203 719</li>
      <li>Email : tka@poralink.net.au</li>
    </ul>
    <p class="back-sectors">Residential • Commercial • Industrial</p>
    <p class="back-rec">Data REC: 61372</p>
    <div class="service-band">
      New Installations | Additions | Rewiring | Repairs | Maintenance<br>
      24 Hours Faults and Emergency Assistance
    </div>
  </section>

</main>
</body>
</html>
```